Logo + Label Design (Men’s Grooming Brand & Product Packaging)

Design a logo and 2 oz pomade label for Brant, a modern men’s grooming brand focused on clean, high-quality, natural ingredients. The design should establish a bold, masculine, minimalist identity that can later extend to products like shaving gel and body wash.

Key Requirements

Create a primary logo for “Brant” and a core label for the 2 oz pomade jar (screw-top).

Use a clean, modern style — masculine, confident, and approachable (think Wendel’s, Valto, Northfield Mill).

Design for 1–2 color screen printing on solid jar colors (white, black, or navy).

Avoid gradients, foil, or embossing. Must work in black & white.

Provide: vector logo, mockup of the 2 oz jar, color palette (CMYK/RGB/HEX), and font specs.

Winning design may lead to future projects (body wash, shave gel, skincare lines).

Font styles to use
Other font styles liked:
• We like the fonts and design concept in the attached mockup.

Requirements
Should not have
• We want to avoid too much writing or busy designs. We want to avoid having graphics/illustrations embedded in the logo if they will cause the brand to look less classy or sophisticated. We also want the design to look simple and all-American (e.g. Pellham and Stroud, Tall Pine, The BRIM, etc). We’d like to give a Kessler & Dunmore vibe that feels classy and high end.

```html
<!DOCTYPE html>
<html lang="en">
<head>
<meta charset="utf-8">
<title>Brant Men’s Hair Pomade – Label</title>
<link href="https://fonts.googleapis.com/css2?family=Roboto+Slab:wght@800&family=Montserrat:wght@400;700&family=PT+Serif&display=swap" rel="stylesheet">
<style>
  :root {
    --paper: #ffffff;
    --charcoal: #2a2a2a;
    --lid: #333333;
    --ink-white: #f2f2f2;
    --ink-grey: #cfcfcf;
    --band-black: #0c0c0c;
    --accent-blue: #3f78c4;
    --band-blue: #3b73c2;
  }
  html, body {
    margin: 0;
    width: 1200px;
    height: 1200px;
    overflow: hidden;
    background: var(--paper);
  }
  .artboard { display: block; width: 1200px; height: 1200px; }
  .wordmark { font-family: "Roboto Slab", Georgia, serif; font-weight: 800; fill: var(--ink-white); }
  .product-name { font-family: "Montserrat", Arial, sans-serif; font-weight: 700; }
  .scent { font-family: "PT Serif", Georgia, serif; fill: var(--accent-blue); }
  .spec { font-family: "Montserrat", Arial, sans-serif; font-weight: 400; fill: var(--ink-white); }
</style>
</head>
<body>
<svg class="artboard" viewBox="0 0 1200 1200" xmlns="http://www.w3.org/2000/svg">

  <!-- Lid label -->
  <g class="lid-label">
    <circle cx="840" cy="400" r="270" fill="var(--lid)"/>
    <circle cx="840" cy="400" r="246" fill="none" stroke="var(--ink-white)" stroke-width="2"/>
    <text class="wordmark" x="840" y="330" font-size="104" text-anchor="middle">Brant</text>
    <text class="product-name" x="840" y="400" font-size="32" fill="var(--ink-white)" text-anchor="middle" textLength="380" lengthAdjust="spacingAndGlyphs">MEN’S HAIR POMADE</text>
    <rect class="scent-band" x="700" y="420" width="280" height="42" fill="var(--band-black)" stroke="var(--ink-white)" stroke-width="1.5"/>
    <text class="scent" x="840" y="452" font-size="30" text-anchor="middle" textLength="240" lengthAdjust="spacingAndGlyphs">FRESH &amp; CLEAN</text>
    <rect class="hold-band" x="700" y="462" width="280" height="38" fill="var(--band-blue)" stroke="var(--ink-white)" stroke-width="1.5"/>
    <text class="spec" x="840" y="487" font-size="16" text-anchor="middle" textLength="256" lengthAdjust="spacingAndGlyphs">MEDIUM HOLD – MATTE FINISH</text>
    <text class="spec" x="840" y="560" font-size="18" text-anchor="middle">NET WT 2 OZ (57 G)</text>
  </g>

  <!-- Jar side label -->
  <g class="jar-label">
    <rect x="120" y="560" width="610" height="260" rx="18" fill="var(--charcoal)"/>
    <text class="wordmark" x="300" y="705" font-size="96" text-anchor="middle">Brant</text>
    <text class="spec" x="300" y="760" font-size="15" text-anchor="middle">NET WT 2 OZ (57 G)</text>
    <text class="product-name" x="472" y="630" font-size="30" fill="var(--ink-grey)">MEN’S</text>
    <text class="product-name" x="472" y="670" font-size="30" fill="var(--ink-grey)" textLength="226" lengthAdjust="spacingAndGlyphs">HAIR POMADE</text>
    <rect class="scent-band" x="472" y="692" width="228" height="36" fill="var(--band-black)" stroke="var(--ink-grey)" stroke-width="1.2"/>
    <text class="scent" x="586" y="719" font-size="24" text-anchor="middle" textLength="190" lengthAdjust="spacingAndGlyphs">FRESH &amp; CLEAN</text>
    <rect class="hold-band" x="472" y="728" width="228" height="30" fill="var(--band-blue)" stroke="var(--ink-grey)" stroke-width="1.2"/>
    <text class="spec" x="586" y="748" font-size="13" text-anchor="middle" textLength="208" lengthAdjust="spacingAndGlyphs">MEDIUM HOLD – MATTE FINISH</text>
  </g>

</svg>
</body>
</html>
```